Fern Lodge Painting, Eco and Non toxic painting client information brochure.

Fern lodge painting is a painting company that specialises in eco and non toxic paints. This brochure will be left with the client after the initial meeting to explain about my business and hopefully win the job. By reading the text i have provided (see attachment) you can get a better understanding of what we do.
The brochure should be fresh and clean looking, complimenting the Fern Lodge Painting logo and the text provided.
This will be printed onto a recycled paper.
Text and font must clear and easy to read.

Please have a look at my web page. I will be redoing this soon as well but this will give you some ideas of where I'm at.

Would like some picture but not sure what.
I have attached some pics but they don't have to be use
Updates

Hi peeps,

Thanks for all the great designs and sorry i haven't got back to you sooner.
been a bit busy.
Tomorrow i hope to be able to sit down and have a good look at what everybody has done.
Thanks again i really appreciate the effort.

kind regards gordon 

hi designers,

Just sat down and had a good look at the designs sent in and there are some crackers.
Its going to be very difficult to choose. I have only 1 day left before it closes so ill wait till then to see if there are any more submissions come in then ill get back to everybody.
Thanks again for your time and effort.

kind regards gordon 

Hi too all you designers that have worked on my project. 

I am always amazed at all the different designs that come through. Super work guys and girls. 
I have narrowed it down to a couple of designs.
Ill be making the decision tonight.
Thanks again to you all and i really appreciate all the hard work.
I will be doing another brochure in the future for more architecture / builder focus and there were a few designs that would work perfectly for this.

Kinds regards gordon  

Target Market(s)

The work we do is mainly residential repaints, family homes
Mostly I am dealing with the wife of the family or female designers/architects

Industry/Entity Type

Painting

Requirements
Must have
• Company logo, either white or black version what ever suits best.
Text that has been provided.
Brochure will be 1 page A 4, folded into 3 parts both sides.
Front page must have logo and
SPECIALSING IN:
NON TOXIC
ECO FRIENDLY &
HEAT REFLECTIVE PAINTS
Phone 040 318 2694
Painting@fernlodge.biz
www.fernlodge.biz

```html
<!DOCTYPE html>
<html lang="en">
<head>
<meta charset="utf-8">
<title>Fern Lodge Painting – Client Brochure</title>
<link rel="stylesheet" href="https://fonts.googleapis.com/css2?family=Exo+2:wght@500;600;700&display=swap">
<style>
  :root {
    --leaf-green: #8dc63f;
    --leaf-pale: #e6f2d4;
    --handle-black: #1e1e1e;
    --ink-black: #000000;
    --frame-grey: #3a3a3a;
    --paper-white: #ffffff;
  }
  * { box-sizing: border-box; margin: 0; padding: 0; }
  html, body {
    width: 846px; height: 1200px; overflow: hidden;
    background: var(--paper-white);
  }
  body {
    position: relative;
    font-family: "Exo 2", sans-serif;
    color: var(--leaf-green);
  }
  .spread {
    position: absolute;
    left: 22px; width: 802px;
    border: 3px solid var(--frame-grey);
    background: var(--paper-white);
    overflow: hidden;
  }
  .spread--outside { top: 20px; height: 572px; }
  .spread--inside { top: 604px; height: 576px; }

  .cover-panel {
    position: absolute; top: 0; right: 0; bottom: 0;
    left: 272px;
    background: var(--ink-black);
  }

  .text-block {
    position: absolute;
    font-size: 9.8px;
    line-height: 11.6px;
    font-weight: 600;
  }
  .text-block h2 {
    font-size: 11.6px;
    font-weight: 700;
    letter-spacing: 0.2px;
    text-transform: uppercase;
    margin-bottom: 10px;
    line-height: 13.5px;
  }
  .text-block p + p { margin-top: 11.6px; }

  .about-business { left: 34px; top: 73px; width: 205px; }

  .brand {
    position: absolute; left: 273px; top: 372px; width: 240px;
    text-align: center;
  }
  .brand__name {
    display: flex; align-items: center; justify-content: center; gap: 7px;
    color: var(--paper-white);
    font-weight: 700; font-size: 16px; letter-spacing: 0.4px;
    text-transform: uppercase;
  }
  .brand__mark { width: 13px; height: 13px; background: var(--leaf-green); }
  .brand__tagline {
    margin-top: 16px;
    color: var(--paper-white);
    font-size: 8.2px; line-height: 10.4px; font-weight: 700;
  }
  .brand__contact {
    margin-top: 10px;
    color: var(--leaf-green);
    font-size: 8.2px; line-height: 10px; font-weight: 700;
  }
  .brand__web {
    margin-top: 12px;
    color: var(--leaf-green);
    font-size: 8.2px; font-weight: 700;
  }

  .roller-artwork {
    position: absolute; left: 0; top: 305px;
    width: 500px; height: 271px;
    background: linear-gradient(to bottom,
      var(--leaf-green) 0%,
      var(--leaf-green) 58%,
      var(--leaf-pale) 62%,
      var(--paper-white) 100%);
    border-top-right-radius: 14px;
  }

  .about-owner { left: 290px; top: 70px; width: 180px; }
  .hiring { left: 290px; top: 190px; width: 205px; }
  .going-green { left: 555px; top: 70px; width: 190px; }
  .vocs { left: 555px; top: 190px; width: 190px; }
</style>
</head>
<body>

<section class="spread spread--outside" aria-label="Brochure outside">
  <div class="text-block about-business">
    <h2>About the business</h2>
    <p>At Fern Lodge Painting we provide a high-quality service and exceptional craftsmanship for both domestic and commercial projects. We are proud to say we are making our work practices and business support processes more sustainable. We want to be sure we are doing our part to reduce our carbon footprint.</p>
    <p>We take the time to research alternative eco painting products and processes. We can also provide you with information about the products and why we use them. All our jobs are professionally finished utilising only the best tools and products available.</p>
    <p>We aim to limit the interruption to clients and their families as a result of our work; safety is paramount. We make sure that you are satisfied with the work done and will communicate with you throughout the job.</p>
    <p>Fern Lodge Painting is dedicated to learning, understanding and implementing new products and techniques that will be safer for the environment and your family. All this is done at a competitive price</p>
  </div>

  <div class="cover-panel">
    <div class="brand">
      <div class="brand__name"><span class="brand__mark"></span>Fern Lodge Painting</div>
      <p class="brand__tagline">Specialising in Non Toxic,<br>Eco Friendly &amp; Heat Reflective Paints</p>
      <p class="brand__contact">040 318 2694<br>painting@fernlodge.biz</p>
      <p class="brand__web">www.fernlodge.biz</p>
    </div>
  </div>
</section>

<section class="spread spread--inside" aria-label="Brochure inside">
  <div class="roller-artwork" role="img" aria-label="Illustration of a paint roller with a green roller sleeve over a pattern of green leaves"></div>

  <div class="text-block about-owner">
    <h2>About the owner</h2>
    <p>Gordon Reid has been painting for over 20 years. He is an accredited Green Painter and is often called upon by architects and builders to provide advice on sustainable products and methods.</p>
  </div>

  <div class="text-block hiring">
    <h2>Hiring a professional</h2>
    <p>Hiring a professional painter is never an easy decision and one not to be taken lightly. Painting is a highly skilled trade and it takes considerable experience and expertise to obtain a high quality finish.</p>
  </div>

  <div class="text-block going-green">
    <h2>Going green</h2>
    <p>We can help you make smart decisions about creating a better environment and further minimizing any risk for your family and the spaces we live in. This can be achieved reducing the amount of VOCs (volatile organic compounds) by selecting the correct products.</p>
  </div>

  <div class="text-block vocs">
    <h2>VOCs = Volatile organic compounds</h2>
    <p>VOCs are hazardous chemicals that are emitted from paints. This occurs even after the paint has dried; paints can continue too emit VOCs for several years after application. By using low VOC emitting paints, fewer chemicals are rleased than traditional paints.</p>
    <p>In choosing a zero VOC option, you will experience no odour after the paint has dried and will be helping improve air quality both inside and outside your home or business.</p>
    <p>At Fern Lodge Painting we choose to use these products and a green business approach because we care about our clients, workers and the overall environment. We can help make a difference, not just by changing the colour of your home or business but by giving you a better, safer environment in which to live and work.</p>
  </div>
</section>

</body>
</html>
```